Vantor Medica Innovative Business Card

Stunning business card. Background will be black. Letters in gold. Modern yet simple design that is attention grabbing. QR code leading to site. Attractive primarily to males ages 30 to 50 but also to females in same age range looking for beauty and mental health products

Target Market(s)

Males in the 30-50 age demographics

Industry/Entity Type

Pharmaceuticals selling erectile dysfunction and mens health medications

Contact Information for Business Card

www.vantormedica.example; (775) BUY-KELO; info@vantormedica.example

Colors
FFC000
F8CF3A
FAE287
FDF2CF
FEFAEE

Requirements
Must have
• Black business card with gold letters.
Nice to have
• perhaps just the logo or the "R" icon by itself on one side
Should not have
• too much content so it does not look busy

```html
<!DOCTYPE html>
<html lang="en">
<head>
<meta charset="UTF-8">
<title>Vantor Medica Business Card</title>
<link rel="stylesheet" href="https://fonts.googleapis.com/css2?family=Poppins:wght@400;500;600&family=Quicksand:wght@500;600&display=swap">
<style>
  :root {
    --page: #ffffff;
    --card-dark: #030303;
    --card-mid: #1b1b1b;
    --gold: #d6b23e;
    --gold-soft: #c9a53a;
    --gold-line: #d9b83f;
  }
  * { box-sizing: border-box; margin: 0; padding: 0; }
  html, body {
    width: 1200px; height: 714px; overflow: hidden;
    background: var(--page);
  }
  .canvas { position: relative; width: 1200px; height: 714px; }
  .card {
    position: absolute; top: 216px;
    width: 468px; height: 280px;
    border-radius: 14px; overflow: hidden;
    background: linear-gradient(115deg, #0b0b0b 0%, var(--card-mid) 32%, #050505 52%, var(--card-dark) 62%, #151515 84%, #080808 100%);
  }
  .card--front { left: 111px; }
  .card--back { left: 620px; }

  .brand-name {
    position: absolute;
    font-family: "Poppins", sans-serif;
    font-weight: 600;
    color: var(--gold);
    white-space: nowrap;
    letter-spacing: 0.5px;
    transform: translateX(-50%);
  }
  .card--front .brand-name { left: 234px; top: 122px; font-size: 30px; }
  .card--back .brand-name { left: 117px; top: 106px; font-size: 24px; }

  .front-rule {
    position: absolute; left: 0; right: 2px; top: 237px;
    height: 4px; border-radius: 2px; background: var(--gold-line);
  }
  .front-site {
    position: absolute; left: 0; right: 0; top: 256px;
    text-align: center;
    font-family: "Quicksand", sans-serif; font-weight: 600;
    font-size: 14px; color: var(--gold); letter-spacing: 0.3px;
  }

  .back-divider {
    position: absolute; left: 232px; top: 58px;
    width: 3px; height: 164px; border-radius: 2px; background: var(--gold-soft);
  }
  .person { position: absolute; left: 270px; top: 60px; }
  .person-name {
    font-family: "Poppins", sans-serif; font-weight: 500;
    font-size: 30px; line-height: 1; color: var(--gold); letter-spacing: 1px;
  }
  .person-role {
    font-family: "Poppins", sans-serif; font-weight: 400;
    font-size: 14px; line-height: 1.2; color: var(--gold-soft); margin-top: 2px;
  }
  .contacts { position: absolute; left: 271px; top: 148px; list-style: none; }
  .contact {
    display: flex; align-items: center; height: 21px;
    font-family: "Quicksand", sans-serif; font-weight: 600;
    font-size: 11px; color: var(--gold);
  }
  .contact-icon { width: 18px; height: 18px; margin-right: 11px; flex: none; }
</style>
</head>
<body>
<main class="canvas">
  <section class="card card--front">
    <div class="brand-name">Vantor Medica</div>
    <div class="front-rule"></div>
    <p class="front-site">www.vantormedica.example</p>
  </section>

  <section class="card card--back">
    <div class="brand-name">Vantor Medica</div>
    <div class="back-divider"></div>
    <div class="person">
      <h1 class="person-name">User Name</h1>
      <p class="person-role">General Manager</p>
    </div>
    <ul class="contacts">
      <li class="contact">
        <svg class="contact-icon" viewBox="0 0 20 20" aria-hidden="true">
          <circle cx="10" cy="10" r="10" fill="#d6b23e"/>
          <path d="M6.4 5.2l1.8-.4 1.1 2.5-1.2 1c.6 1.3 1.5 2.2 2.8 2.8l1-1.2 2.5 1.1-.4 1.8c-.2.6-.7.9-1.3.9C8.9 13.5 6.5 11.1 6.3 6.5c0-.6.4-1.1.1-1.3z" fill="#0b0b0b"/>
        </svg>
        (775) BUY-KELO
      </li>
      <li class="contact">
        <svg class="contact-icon" viewBox="0 0 20 20" aria-hidden="true">
          <circle cx="10" cy="10" r="10" fill="#d6b23e"/>
          <rect x="5" y="6.5" width="10" height="7" fill="none" stroke="#0b0b0b" stroke-width="1.2"/>
          <path d="M5 6.5l5 4 5-4M5 13.5l3.7-3.6M15 13.5l-3.7-3.6" fill="none" stroke="#0b0b0b" stroke-width="1.1"/>
        </svg>
        info@vantormedica.example
      </li>
      <li class="contact">
        <svg class="contact-icon" viewBox="0 0 20 20" aria-hidden="true">
          <circle cx="10" cy="10" r="10" fill="#d6b23e"/>
          <path d="M10 4.5a3.6 3.6 0 0 0-3.6 3.6c0 2.7 3.6 7 3.6 7s3.6-4.3 3.6-7A3.6 3.6 0 0 0 10 4.5z" fill="#0b0b0b"/>
          <circle cx="10" cy="8.1" r="1.3" fill="#d6b23e"/>
        </svg>
        xyz
      </li>
    </ul>
  </section>
</main>
</body>
</html>
```